Dorsey K. Wendell Business Card

We need a business card for our company Dorsey K. Wendell Heating & Plumbing to be distributed to potential customers. It should follow the color scheme of our logo and have a modern upscale and masculine look.

The logo is attached and the info below should also be included:

5187 W. Cedar Brook Rd.
Brookvale, PA 17298

Russell T. Wendell
(717) 592-0817
russelltwendell@fernmail.net
dorseykwendell.net
PA #093148

Industry/Entity Type

Business

Contact Information for Business Card

5187 W. Cedar Brook Rd.
Brookvale, PA 17298

Russell T. Wendell
(717) 592-0817
russelltwendell@fernmail.net
dorseykwendell.net
PA #093148

Colors

Designer to choose colors to be used in the design.

Requirements
Must have
• Information above included

```html
<!DOCTYPE html>
<html lang="en">
<head>
<meta charset="utf-8">
<title>Dorsey K. Wendell Business Card</title>
<link rel="stylesheet" href="https://fonts.googleapis.com/css2?family=Oswald:wght@500;600&family=Lato:wght@700;900&display=swap">
<style>
  :root {
    --stage: #111111;
    --card: #ffffff;
    --brand-blue: #2a5bab;
    --brand-blue-deep: #1d57a6;
    --brand-green: #a8d143;
    --ink: #1e1e1e;
  }
  * { box-sizing: border-box; margin: 0; padding: 0; }
  html, body { width: 1200px; height: 1000px; overflow: hidden; }
  body {
    background: var(--stage);
    position: relative;
    font-family: "Lato", Arial, sans-serif;
  }
  .card {
    position: absolute;
    top: 352px;
    width: 520px;
    height: 297px;
    background: var(--card);
    overflow: hidden;
  }
  .card--front { left: 50px; }
  .card--back { left: 630px; }

  /* Front */
  .brand {
    position: absolute;
    left: 60px;
    top: 112px;
    display: flex;
    align-items: center;
    gap: 16px;
  }
  .brand__square {
    width: 66px;
    height: 66px;
    background: var(--brand-blue);
    flex: none;
  }
  .brand__name {
    font-family: "Oswald", Arial, sans-serif;
    font-weight: 600;
    color: var(--brand-blue);
    text-transform: uppercase;
    font-size: 30px;
    line-height: 1.05;
    letter-spacing: 0.5px;
  }

  /* Back */
  .contact {
    position: absolute;
    left: 30px;
    top: 28px;
  }
  .contact__name {
    font-family: "Oswald", Arial, sans-serif;
    font-weight: 600;
    color: var(--brand-blue);
    text-transform: uppercase;
    font-size: 20px;
    letter-spacing: 0.5px;
  }
  .contact__address {
    margin-top: 4px;
    font-weight: 700;
    color: var(--ink);
    font-size: 13px;
    line-height: 1.25;
  }
  .contact__license {
    margin-top: 14px;
    font-family: "Oswald", Arial, sans-serif;
    font-weight: 600;
    color: var(--brand-blue);
    font-size: 22px;
  }
  .contact__list {
    list-style: none;
    margin-top: 6px;
  }
  .contact__item {
    display: flex;
    align-items: center;
    gap: 9px;
    font-weight: 700;
    color: var(--ink);
    font-size: 13.5px;
    line-height: 1.5;
  }
  .contact__icon { width: 12px; height: 12px; flex: none; }
  .panel {
    position: absolute;
    right: 0;
    top: 58px;
    width: 205px;
    height: 186px;
    background: linear-gradient(135deg, var(--brand-blue), var(--brand-blue-deep));
  }
  .band {
    position: absolute;
    left: 0;
    bottom: 0;
    width: 100%;
    height: 18px;
    background: var(--brand-green);
  }
</style>
</head>
<body>
  <section class="card card--front" aria-label="Business card front">
    <div class="brand">
      <span class="brand__square" aria-hidden="true"></span>
      <p class="brand__name">Dorsey K. Wendell<br>Heating &amp; Plumbing</p>
    </div>
  </section>

  <section class="card card--back" aria-label="Business card back">
    <div class="contact">
      <h1 class="contact__name">Russell T. Wendell</h1>
      <p class="contact__address">5187 W. Cedar Brook Rd.<br>Brookvale, PA 17298</p>
      <p class="contact__license">PA #093148</p>
      <ul class="contact__list">
        <li class="contact__item">
          <svg class="contact__icon" viewBox="0 0 24 24" aria-hidden="true"><path fill="#2a5bab" d="M6.6 10.8c1.4 2.8 3.8 5.1 6.6 6.6l2.2-2.2c.3-.3.7-.4 1-.2 1.1.4 2.3.6 3.6.6.6 0 1 .4 1 1V20c0 .6-.4 1-1 1C10.6 21 3 13.4 3 4c0-.6.4-1 1-1h3.5c.6 0 1 .4 1 1 0 1.3.2 2.5.6 3.6.1.3 0 .7-.2 1z"/></svg>
          (717) 592-0817
        </li>
        <li class="contact__item">
          <svg class="contact__icon" viewBox="0 0 24 24" aria-hidden="true"><path fill="#2a5bab" d="M2 5h20v14H2z"/><path fill="none" stroke="#fff" stroke-width="2" d="M2 5l10 8 10-8"/></svg>
          russelltwendell@fernmail.net
        </li>
        <li class="contact__item">
          <svg class="contact__icon" viewBox="0 0 24 24" aria-hidden="true"><g fill="none" stroke="#2a5bab" stroke-width="2"><circle cx="12" cy="12" r="10"/><ellipse cx="12" cy="12" rx="4" ry="10"/><path d="M2 12h20"/></g></svg>
          dorseykwendell.net
        </li>
      </ul>
    </div>
    <div class="panel" aria-hidden="true"></div>
    <div class="band" aria-hidden="true"></div>
  </section>
</body>
</html>
```